VORN - Business cards

Business card to be created for Commercial sales staff

Target Market(s)

Commercial businesses

Industry/Entity Type

Commercial

Contact Information for Business Card

Look professional. For commercial clients

Colors
ffffff

Requirements
Must have
• - Vorn Logo
• - Commercial sales staff as postion
• - room for commerical sales manager role
• - person name and their mobile number
• - Website : vornelectrical.com.au
Nice to have
• White background.
• On back of business card just have the logo no other information
Should not have
• Should only have white background on front of card.

```html
<!DOCTYPE html>
<html lang="en">
<head>
<meta charset="utf-8">
<title>VORN – Business cards</title>
<link rel="stylesheet" href="https://fonts.googleapis.com/css2?family=Exo+2:wght@400;700;800&display=swap">
<style>
  :root {
    --red: #c40e18;
    --red-deep: #a80c14;
    --charcoal: #33363d;
    --text: #3a3a3a;
    --white: #ffffff;
    --stage: #2e2e2e;
    --faint: #f3f3f3;
  }
  * { box-sizing: border-box; margin: 0; padding: 0; }
  html, body { width: 1200px; height: 900px; overflow: hidden; }
  body {
    background: var(--stage);
    font-family: "Exo 2", sans-serif;
    position: relative;
  }
  .card {
    position: absolute;
    width: 514px;
    height: 296px;
    background: var(--white);
    overflow: hidden;
  }
  .card--back-white { left: 72px; top: 138px; }
  .card--back-red { left: 615px; top: 138px; background: var(--red); }
  .card--front-plain { left: 72px; top: 465px; }
  .card--front-band { left: 615px; top: 465px; }

  .decor-circle {
    position: absolute;
    left: -10px; top: 20px;
    width: 330px; height: 330px;
    border-radius: 50%;
    background: var(--faint);
  }
  .card--back-red .decor-circle { background: var(--red-deep); }

  .wordmark {
    position: absolute;
    display: flex;
    align-items: center;
    gap: 10px;
    font-weight: 800;
    color: var(--charcoal);
    line-height: 1;
  }
  .wordmark__dot {
    border-radius: 50%;
    background: var(--red);
    flex: none;
  }
  .wordmark--large { right: 34px; bottom: 38px; font-size: 50px; letter-spacing: 1px; }
  .wordmark--large .wordmark__dot { width: 44px; height: 44px; }
  .card--back-red .wordmark { color: var(--white); }
  .card--back-red .wordmark__dot { background: var(--white); }

  .mark-circle {
    position: absolute;
    width: 150px; height: 150px;
    border-radius: 50%;
    background: var(--red);
  }
  .card--front-plain .mark-circle { left: 52px; top: 80px; }
  .card--front-band .mark-circle { left: 52px; top: 82px; }

  .divider {
    position: absolute;
    left: 248px;
    width: 1px;
    background: var(--charcoal);
  }
  .card--front-plain .divider { top: 58px; height: 180px; }
  .card--front-band .divider { left: 251px; top: 58px; height: 184px; }

  .details {
    position: absolute;
    left: 273px;
    color: var(--text);
    font-size: 11.5px;
    line-height: 15.5px;
  }
  .card--front-plain .details { top: 55px; }
  .card--front-band .details { left: 276px; top: 55px; }

  .details__name { font-size: 16px; font-weight: 400; letter-spacing: .5px; color: var(--charcoal); line-height: 20px; }
  .details__role { color: var(--red); font-size: 11.5px; margin-bottom: 15px; }
  .contact-list { list-style: none; margin-bottom: 14px; }
  .contact-list li { display: flex; align-items: center; gap: 7px; }
  .contact-list svg { width: 10px; height: 10px; fill: var(--red); flex: none; }
  .wordmark--small { position: static; font-size: 17px; gap: 5px; margin-bottom: 4px; }
  .wordmark--small .wordmark__dot { width: 14px; height: 14px; }
  .details__web { color: var(--red); }

  .footer-band {
    position: absolute;
    left: 0; bottom: 0;
    width: 100%; height: 36px;
  }
  .footer-band__web {
    position: absolute;
    left: 0; right: 0; bottom: 9px;
    text-align: center;
    color: var(--white);
    font-size: 11.5px;
    padding-left: 20px;
  }
</style>
</head>
<body>

  <section class="card card--back-white" aria-label="Card back, white">
    <div class="decor-circle"></div>
    <div class="wordmark wordmark--large"><span class="wordmark__dot"></span>VORN</div>
  </section>

  <section class="card card--back-red" aria-label="Card back, red">
    <div class="decor-circle"></div>
    <div class="wordmark wordmark--large"><span class="wordmark__dot"></span>VORN</div>
  </section>

  <section class="card card--front-plain" aria-label="Card front">
    <div class="mark-circle"></div>
    <div class="divider"></div>
    <div class="details">
      <p class="details__name">DANIEL MARLOW</p>
      <p class="details__role">managing director</p>
      <ul class="contact-list">
        <li><svg viewBox="0 0 10 10"><path d="M1 4c0-2 2-3 4-3s4 1 4 3l-2 1-1-1.5H4L3 5z M2 6h6v3H2z"/></svg>888 888 88 88</li>
        <li><svg viewBox="0 0 10 10"><path d="M3 0h4a1 1 0 0 1 1 1v8a1 1 0 0 1-1 1H3a1 1 0 0 1-1-1V1a1 1 0 0 1 1-1zm0 1.5v6h4v-6z"/></svg>555 555 55 55</li>
        <li><svg viewBox="0 0 10 10"><path d="M0 2h10v1L5 6 0 3z M0 4l5 3 5-3v4H0z"/></svg>d.marlow@vornelectrical.com.au</li>
      </ul>
      <div class="wordmark wordmark--small"><span class="wordmark__dot"></span>VORN</div>
      <p>123 Fake Street</p>
      <p>Anytown, New York 12345</p>
      <p class="details__web">www.vornelectrical.com.au</p>
    </div>
  </section>

  <section class="card card--front-band" aria-label="Card front with footer band">
    <div class="mark-circle"></div>
    <div class="divider"></div>
    <div class="details">
      <p class="details__name">DANIEL MARLOW</p>
      <p class="details__role">managing director</p>
      <ul class="contact-list">
        <li><svg viewBox="0 0 10 10"><path d="M1 4c0-2 2-3 4-3s4 1 4 3l-2 1-1-1.5H4L3 5z M2 6h6v3H2z"/></svg>888 888 88 88</li>
        <li><svg viewBox="0 0 10 10"><path d="M3 0h4a1 1 0 0 1 1 1v8a1 1 0 0 1-1 1H3a1 1 0 0 1-1-1V1a1 1 0 0 1 1-1zm0 1.5v6h4v-6z"/></svg>555 555 55 55</li>
        <li><svg viewBox="0 0 10 10"><path d="M0 2h10v1L5 6 0 3z M0 4l5 3 5-3v4H0z"/></svg>d.marlow@vornelectrical.com.au</li>
      </ul>
      <div class="wordmark wordmark--small"><span class="wordmark__dot"></span>VORN</div>
      <p>123 Fake Street</p>
      <p>Anytown, New York 12345</p>
    </div>
    <svg class="footer-band" viewBox="0 0 514 36" preserveAspectRatio="none" aria-hidden="true">
      <polygon points="0,16 150,16 142,36 0,36" fill="var(--charcoal)"/>
      <polygon points="372,16 514,16 514,36 380,36" fill="var(--charcoal)"/>
      <polygon points="160,3 358,3 368,36 150,36" fill="var(--red)"/>
    </svg>
    <p class="footer-band__web">www.vornelectrical.com.au</p>
  </section>

</body>
</html>
```